Singer Kemiro needs a CD cover photoshopping for a new song "Drift"

Hi. My name is Kemiro. I need a CD cover artwork for my new song "Drift". I would like to use my real face photo as a base this time and designers to photoshop it into a cool CD cover. I aim to have an illustration type face image.

Examples are:
https://www.beatloopzine.com/2017/01/owen-parrick-releases-first-four-song-wave-of-new-album-the-road-past-nowhere/

or

https://soundshelfy.com/us/album/marble/8842019375

The image doesn't need to be too artistic like above two images. I need a simple face illustration image. Although the song title is "Drift", I want my face looking a little bit sad with my eyes closed. My name "Kemiro" and song's title "Drift" are necessary to be written. jpg file is necessary. Thank you.
Kemiro

Target Market(s)

Music industry

Requirements
Must have
• My name: Kemiro
• Song title: Drift
• My face illustration illustrated with my real face photo (looking a little bit sad with my eyes closed)
Nice to have
• Photoshopping my face to look a little bit more good looking
Should not have
• Stock images,

```html
<!DOCTYPE html>
<html lang="en">
<head>
<meta charset="utf-8">
<title>Kemiro – Drift</title>
<link rel="stylesheet" href="https://fonts.googleapis.com/css2?family=Kaushan+Script&display=swap">
<style>
  :root {
    --backdrop: #575a59;
    --sleeve: #ffffff;
    --ink: #111111;
    --title-light: #ffffff;
    --warm: #f4643a;
    --ember: #e94b6a;
    --violet: #5a3f8f;
    --indigo: #2d2f6e;
    --teal: #3f8fc0;
    --mist: #a9c6e6;
  }
  html, body {
    margin: 0;
    padding: 0;
    width: 1200px;
    height: 900px;
    overflow: hidden;
    background: var(--backdrop);
  }
  .canvas {
    position: relative;
    width: 1200px;
    height: 900px;
  }
  .cover {
    position: absolute;
    left: 180px;
    top: 30px;
    width: 840px;
    height: 840px;
    background: var(--sleeve);
    overflow: hidden;
  }
  .portrait {
    position: absolute;
    left: 108px;
    top: 160px;
    width: 626px;
    height: 660px;
    background:
      radial-gradient(ellipse 32% 36% at 48% 42%, var(--indigo) 0%, rgba(45,47,110,0.7) 60%, transparent 100%),
      linear-gradient(100deg, var(--mist) 0%, var(--warm) 18%, var(--ember) 34%, var(--violet) 55%, var(--indigo) 68%, var(--teal) 84%, var(--mist) 100%);
    -webkit-mask-image: radial-gradient(ellipse 50% 50% at 50% 50%, #000 58%, transparent 100%);
    mask-image: radial-gradient(ellipse 50% 50% at 50% 50%, #000 58%, transparent 100%);
  }
  .artist-name,
  .song-title {
    position: absolute;
    left: 0;
    width: 100%;
    margin: 0;
    text-align: center;
    font-family: "Kaushan Script", cursive;
    font-weight: 400;
    line-height: 1;
  }
  .artist-name {
    top: 34px;
    font-size: 132px;
    letter-spacing: 2px;
    color: var(--ink);
    text-transform: uppercase;
  }
  .song-title {
    top: 680px;
    font-size: 96px;
    color: var(--title-light);
  }
</style>
</head>
<body>
  <main class="canvas">
    <section class="cover">
      <div class="portrait" role="img" aria-label="Illustrated portrait of the singer with eyes closed, wrapped in orange, violet and blue smoke"></div>
      <h1 class="artist-name">Kemiro</h1>
      <h2 class="song-title">Drift</h2>
    </section>
  </main>
</body>
</html>
```